Photography Business, Business Card

Looking for a unique cutting edge card that takes advantage of the latest printing technologies. Please review this site for all the options they office: https://plumeprints.example. If you can think it they can do it. And if you have an idea and do not know if they can do it, I will check into it.
Updates

Target Market(s)

People and places I took images of and future clients.

Industry/Entity Type

Photography

Contact Information for Business Card

Name, cell & email. Colin Hartley, chartley@kvnphoto.example, 318-742-9061

Colors

Designer to choose only greyscale colors for use in the design.

Requirements
Must have
• 100% cutting edge. Is so great, those I hand it to always show it to someone else. A piece of art.
Nice to have
• Blacks, silvers, greys, some red. Maybe other colors?

```html
<!DOCTYPE html>
<html lang="en">
<head>
<meta charset="utf-8">
<title>Kestrel Vane Media – Business Card</title>
<link href="https://fonts.googleapis.com/css2?family=Poppins:wght@400;500;600;700;800&display=swap" rel="stylesheet">
<style>
  :root {
    --backdrop: #1b1b1b;
    --card-dark: #212121;
    --card-light: #333333;
    --accent-red: #ec1c24;
    --bracket: #111111;
    --white: #ffffff;
    --lens-dark: #141414;
    --lens-mid: #262626;
  }
  * { margin: 0; padding: 0; box-sizing: border-box; }
  html, body {
    width: 1200px; height: 1000px; overflow: hidden;
    background: var(--backdrop);
    font-family: "Poppins", sans-serif;
  }
  .canvas { position: relative; width: 1200px; height: 1000px; }

  .card {
    position: absolute; left: 282px; width: 636px; height: 362px; overflow: hidden;
    background: linear-gradient(125deg, var(--card-dark) 0%, var(--card-dark) 22%, var(--card-light) 38%, var(--card-dark) 58%, #272727 78%, var(--card-light) 100%);
  }
  .card--front { top: 105px; }
  .card--back { top: 531px; }

  .frame { position: absolute; }
  .frame svg { display: block; width: 100%; height: 100%; }

  .lens-art {
    position: absolute;
    background: linear-gradient(90deg, var(--lens-mid), var(--lens-dark) 30%, var(--lens-mid) 55%, var(--lens-dark) 80%, var(--lens-mid));
    border-radius: 4px;
  }

  /* front */
  .card--front .frame { left: 54px; top: 101px; width: 279px; height: 177px; }
  .brand-name {
    position: absolute; left: 54px; top: 146px; width: 279px;
    text-align: center; color: var(--accent-red);
    font-weight: 700; font-size: 30px; line-height: 1.12; letter-spacing: 1px;
  }
  .card--front .lens-art { left: 376px; top: 119px; width: 237px; height: 125px; }
  .studio-name {
    position: absolute; right: 60px; top: 298px;
    color: var(--accent-red); font-weight: 500; font-size: 11px; letter-spacing: 1.5px;
    text-transform: uppercase;
  }

  /* back */
  .name-band {
    position: absolute; left: 0; top: 0; width: 100%; height: 73px;
    background: var(--accent-red);
    display: flex; align-items: center; justify-content: center;
  }
  .name-band h1 {
    color: var(--white); font-weight: 800; font-size: 42px; letter-spacing: 3px; line-height: 1;
  }
  .card--back .lens-art { left: 21px; top: 111px; width: 237px; height: 124px; }
  .card--back .frame { left: 301px; top: 93px; width: 280px; height: 177px; }
  .tagline {
    position: absolute; left: 301px; top: 93px; width: 280px; height: 177px;
    display: flex; flex-direction: column; align-items: center; justify-content: center;
    color: var(--accent-red); text-align: center;
  }
  .tagline__main { font-weight: 400; font-size: 62px; line-height: 1; }
  .tagline__sub { font-weight: 400; font-size: 31px; line-height: 1.1; }

  .contact {
    position: absolute; top: 298px; display: flex; align-items: center; gap: 10px;
    color: var(--accent-red); font-weight: 500; font-size: 17px;
  }
  .contact--email { left: 76px; }
  .contact--phone { left: 389px; }
  .contact__icon { width: 37px; height: 37px; display: block; }
</style>
</head>
<body>
<div class="canvas">

  <section class="card card--front">
    <div class="frame" aria-hidden="true">
      <svg viewBox="0 0 279 177" fill="none" stroke="var(--bracket)" stroke-width="4">
        <path d="M2 27V2H34M245 2H277V27M2 150V175H34M245 175H277V150"/>
      </svg>
    </div>
    <div class="brand-name">KESTREL VANE<br>MEDIA</div>
    <div class="lens-art" role="img" aria-label="Side-view silhouette of a camera lens in dark grey"></div>
    <div class="studio-name">Colin Hartley Photography</div>
  </section>

  <section class="card card--back">
    <div class="name-band"><h1>Colin Hartley</h1></div>
    <div class="lens-art" role="img" aria-label="Side-view silhouette of a camera lens in dark grey"></div>
    <div class="frame" aria-hidden="true">
      <svg viewBox="0 0 280 177" fill="none" stroke="var(--bracket)" stroke-width="4">
        <path d="M2 27V2H34M246 2H278V27M2 150V175H34M246 175H278V150"/>
      </svg>
    </div>
    <div class="tagline">
      <span class="tagline__main">Creative</span>
      <span class="tagline__sub">Visual Services</span>
    </div>

    <div class="contact contact--email">
      <svg class="contact__icon" viewBox="0 0 37 37" aria-hidden="true">
        <circle cx="18.5" cy="18.5" r="18.5" fill="var(--accent-red)"/>
        <rect x="9" y="12" width="19" height="13" rx="2" fill="var(--white)"/>
        <path d="M9.5 13L18.5 20L27.5 13" fill="none" stroke="var(--accent-red)" stroke-width="1.6"/>
      </svg>
      <span>chartley@kvnphoto.example</span>
    </div>
    <div class="contact contact--phone">
      <svg class="contact__icon" viewBox="0 0 37 37" aria-hidden="true">
        <circle cx="18.5" cy="18.5" r="18.5" fill="var(--accent-red)"/>
        <path d="M13 9c-2 1-3 3-2 6 1.5 5 5 10 9 12 2.5 1.2 4.5 0.5 6-1l-3.5-3.5-2.3 1.3c-2-1-4-4.5-4.8-6.8l2-1.7L15.8 9z" fill="var(--white)"/>
      </svg>
      <span>318-742-9061</span>
    </div>
  </section>

</div>
</body>
</html>
```